Keystone Draftworks - business cards
A set of business cards for a company
Dear designers,
I suggest that we minimize the quantity of red and grey filled areas on the cards.
I favour more the versions where there is more white space and just some colored accents.
In my opinion it looks more appropriate for our corporate customers.
Thanks for your understanding.
It might be a good idea to print a QR code on the back side of the card if it fits logically.
Not necessary but I'd like to see some ideas with and without it.

```html
<!DOCTYPE html>
<html lang="en">
<head>
<meta charset="utf-8">
<title>Keystone Draftworks – business cards</title>
<link href="https://fonts.googleapis.com/css2?family=Roboto:ital,wght@0,400;0,700;0,900;1,700&family=Roboto+Condensed:wght@700&display=swap" rel="stylesheet">
<style>
  :root {
    --backdrop: #9a6a44;
    --card: #ffffff;
    --brand-red: #a6222b;
    --ink: #4a4a4a;
    --ink-soft: #7a7a7a;
    --rule: #c9c9c9;
    --back-top: #b9c0c6;
    --back-bottom: #7d868f;
  }
  * { margin: 0; padding: 0; box-sizing: border-box; }
  html, body { width: 1200px; height: 785px; overflow: hidden; }
  body {
    position: relative;
    background: var(--backdrop);
    font-family: "Roboto", Arial, sans-serif;
    color: var(--ink);
  }
  .card {
    position: absolute;
    width: 528px;
    height: 295px;
    background: var(--card);
    box-shadow: 0 4px 12px rgba(0,0,0,.35);
    overflow: hidden;
  }
  .card--contact { left: 41px; top: 268px; }
  .card--logo { left: 619px; top: 72px; }
  .card--back {
    left: 619px; top: 418px;
    background: linear-gradient(160deg, var(--back-top), var(--back-bottom));
  }

  .brand {
    position: absolute;
    display: flex;
    align-items: center;
    gap: 14px;
  }
  .brand__dot {
    width: 46px; height: 46px;
    border-radius: 50%;
    background: var(--brand-red);
    flex: none;
  }
  .brand__name {
    font-family: "Roboto Condensed", "Arial Narrow", sans-serif;
    font-weight: 700;
    font-size: 38px;
    line-height: 1;
    color: var(--brand-red);
    text-transform: uppercase;
    letter-spacing: .5px;
  }
  .card--contact .brand { left: 48px; top: 52px; }
  .card--logo .brand { left: 50px; top: 116px; }

  .web {
    position: absolute;
    font-weight: 700;
    font-size: 14px;
    letter-spacing: 1.5px;
    color: var(--ink);
  }
  .card--logo .web { left: 156px; bottom: 22px; }
  .card--back .web { left: 156px; bottom: 24px; color: #fff; }

  .address {
    position: absolute;
    left: 34px; top: 138px;
    font-size: 13px;
    color: var(--ink);
  }
  .address-rule {
    position: absolute;
    left: 0; right: 0; top: 162px;
    height: 1px;
    background: var(--rule);
  }
  .accent-bar {
    position: absolute;
    left: 0; top: 162px;
    width: 12px; height: 133px;
    background: var(--brand-red);
  }
  .contacts {
    position: absolute;
    left: 34px; top: 172px;
    list-style: none;
    font-size: 12.5px;
    line-height: 21px;
  }
  .contacts li { display: flex; align-items: center; gap: 7px; }
  .contacts svg { width: 11px; height: 11px; fill: var(--ink); flex: none; }

  .person {
    position: absolute;
    right: 48px; top: 186px;
    text-align: right;
    padding-right: 0;
  }
  .person__name {
    font-weight: 700;
    font-style: italic;
    font-size: 17px;
    color: var(--brand-red);
  }
  .person__role {
    font-style: italic;
    font-size: 12px;
    color: var(--brand-red);
    margin-top: 4px;
  }
  .person-rule {
    position: absolute;
    left: 318px; top: 178px;
    width: 3px; height: 48px;
    background: var(--brand-red);
  }

  .back-mark {
    position: absolute;
    left: 214px; top: 80px;
    width: 100px; height: 100px;
    border-radius: 50%;
    background: var(--brand-red);
  }
</style>
</head>
<body>

<section class="card card--contact" aria-label="Business card, contact side">
  <div class="brand">
    <span class="brand__dot"></span>
    <span class="brand__name">Keystone Draftworks</span>
  </div>
  <p class="address">Larch Lane, 14 Harrowfield, 40217 Norland</p>
  <div class="address-rule"></div>
  <div class="accent-bar"></div>
  <ul class="contacts">
    <li><svg viewBox="0 0 12 12"><path d="M2 1h3l1 3-2 1a7 7 0 0 0 3 3l1-2 3 1v3c-6 0-9-3-9-9z"/></svg>+44 210 555-0148</li>
    <li><svg viewBox="0 0 12 12"><path d="M3 0h6v12H3zM4 1v8h4V1z"/></svg>+44 210 555-0193</li>
    <li><svg viewBox="0 0 12 12"><path d="M1 1h9v6H1zM2 8h9v3H2z"/></svg>+44 210 555-0148</li>
    <li><svg viewBox="0 0 12 12"><path d="M0 2h12v8H0zM1 3l5 4 5-4v-.5H1z"/></svg>t.venner@keystonedw.example</li>
    <li><svg viewBox="0 0 12 12"><path d="M6 0a6 6 0 1 0 0 12A6 6 0 0 0 6 0zm0 1.5a4.5 4.5 0 1 1 0 9 4.5 4.5 0 0 1 0-9z"/></svg>www.keystonedw.example</li>
  </ul>
  <div class="person-rule"></div>
  <div class="person">
    <p class="person__name">Tobias Venner</p>
    <p class="person__role">Director</p>
  </div>
</section>

<section class="card card--logo" aria-label="Business card, logo side">
  <div class="brand">
    <span class="brand__dot"></span>
    <span class="brand__name">Keystone Draftworks</span>
  </div>
  <p class="web">www.keystonedw.example</p>
</section>

<section class="card card--back" aria-label="Business card, back side">
  <span class="back-mark"></span>
  <p class="web">www.keystonedw.example</p>
</section>

</body>
</html>
```